Design for company homepage promoting to the pharmaceutical industry

Our company produces medical education materials and services for the pharmaceutical industry. Our existing website (www.quorvan.net.au) provides more information.
 
We need a homepage design for our new company website we are creating. Our site will not have a great amount of content, we want it to be fast, user friendly and easily adaptable to viewing on any platform, and through any browser. We don't want it over-designed - i.e. no highly animated banner flags, backgrounds, obscure webfonts, too many graphics etc. Attached are files indicating our existing company logo and design. We want the logo and rings to be retained. We've also attached draft copy for the website.
The final website may be designed in Wordpress (still to be confirmed)
 
This is a design to replace the current site (www.quorvan.net.au). Content will also be revised.
Things we don't like about our current design - doesn't use our current branding, is not very exciting, old fashioned 'standard' format, too much content, just doesn't look that good, boring.
 
Examples of sites we like:
www.brelmot.com.au
http://factsheets.wondipaq.com.au/index.html
 
Features we like from these sites - fast, responsive, short and to the point, cross-platform compatible including smartphones, and looks good
 
Main reasons people will visit our site: to find out whether we can provide services they might be looking for, to make a decision on whether they are interested in what we offer so they can get in touch with us, and to get our contact details.
Main thing we want to achieve from website visits is that it looks good enough and provides enough summary information on us so that they want to get in touch with us, to offer us work or to ask us to come in and meet them to provide more info on what we do.
Two most important calls to action from our website
· make the decision that we can do what you are looking for
· get in touch with us.
Updates

Thanks everyone for your submissions. At this stage with the Christmas break upon us, we are yet to finalise our decision, and will make a decision early in the new year. I hope everyone has a good holiday break.
Kind regards
Doug

Target Market(s)

Pharmaceutical industry professionals, marketers and medical professionals.

Industry/Entity Type

Pharmaceutical

Requirements
Must have
• Company logo and rings must be incorporated, company colour - blue - must be in there.
Should not have
• Complex animation or graphics that will slow the upload or limit cross-platform compatability/viewing on smartphones etc.

```html
<!DOCTYPE html>
<html lang="en">
<head>
<meta charset="utf-8">
<title>Quorvan – Healthcare Communication</title>
<link href="https://fonts.googleapis.com/css2?family=Open+Sans:wght@300;400;600&display=swap" rel="stylesheet">
<style>
:root{
  --brand-blue:#0f5a96;
  --brand-blue-dark:#0b3b68;
  --brand-blue-deep:#082e54;
  --accent-blue:#1b67a8;
  --ink:#4a4f55;
  --muted:#8a9097;
  --hero-top:#e9ecef;
  --hero-bottom:#ffffff;
  --team-bg:#eef1f5;
  --map-tone:#d9dcdf;
  --white:#ffffff;
}
*{box-sizing:border-box;margin:0;padding:0}
html,body{width:1200px;height:2180px;overflow:hidden}
body{font-family:"Open Sans",Arial,sans-serif;color:var(--ink);background:var(--white)}

.site-header{height:430px;background:linear-gradient(var(--hero-top),var(--hero-bottom) 75%);position:relative;text-align:center}
.main-nav{display:flex;justify-content:center;gap:4px;padding-top:0}
.main-nav a{display:block;padding:12px 22px;font-size:13px;color:var(--muted);text-decoration:none;background:#f5f6f7;border-bottom:1px solid #dde1e5}
.main-nav a.is-active{background:var(--brand-blue);color:var(--white)}
.brand{margin-top:40px;display:inline-flex;align-items:center;gap:12px;font-size:58px;font-weight:300;color:var(--brand-blue);letter-spacing:1px}
.brand-dot{width:16px;height:16px;border-radius:50%;background:var(--brand-blue)}
.brand-sub{font-size:12px;color:var(--muted);margin-top:2px;letter-spacing:2px;text-transform:uppercase}
.tagline{position:absolute;left:0;right:0;top:325px;font-size:40px;font-weight:300;line-height:1.12;color:var(--accent-blue)}

.services{height:630px;background:var(--brand-blue);color:var(--white);text-align:center;padding-top:56px}
.services-lead{font-size:27px;font-weight:300;line-height:1.3;max-width:760px;margin:0 auto}
.services-intro{font-size:15px;line-height:1.55;max-width:860px;margin:26px auto 0;opacity:.92}
.service-grid{display:flex;justify-content:center;gap:60px;margin-top:50px}
.service{width:190px}
.service-art{width:150px;height:170px;margin:0 auto;border-radius:8px;background:linear-gradient(#2a74b0,#174f82)}
.service p{font-size:13px;line-height:1.45;margin-top:18px}

.prelaunch{height:260px;text-align:center;padding-top:44px}
.prelaunch h2{font-size:30px;font-weight:300;color:var(--accent-blue)}
.prelaunch p{font-size:13px;line-height:1.6;color:var(--muted);max-width:900px;margin:22px auto 0}

.team{height:260px;background:var(--team-bg);text-align:center;padding-top:34px}
.team h2{font-size:32px;font-weight:300;color:var(--accent-blue)}
.team-list{display:flex;justify-content:center;gap:64px;margin-top:26px}
.member-photo{width:100px;height:100px;border-radius:50%;background:linear-gradient(#c9ced4,#9aa2ab);margin:0 auto;border:3px solid var(--white)}
.member-name{font-size:17px;color:var(--brand-blue);margin-top:10px}
.member-role{font-size:11px;color:var(--muted)}

.location{height:340px;position:relative;background:linear-gradient(135deg,#e4e6e8,var(--map-tone))}
.address-card{position:absolute;left:820px;top:120px;width:340px;padding:18px 22px;background:var(--brand-blue-dark);color:var(--white);font-size:16px;line-height:1.45}

.site-footer{height:260px;background:var(--brand-blue-deep);color:#c9d6e4;padding:26px 70px 0}
.footer-cols{display:flex;justify-content:space-between}
.footer-col h3{font-size:14px;font-weight:600;color:var(--white);margin-bottom:8px}
.footer-col li{list-style:none;font-size:11px;line-height:1.6}
.social li{display:flex;align-items:center;gap:8px}
.social span{width:14px;height:14px;border-radius:50%;background:#5f86b0}
.footer-bar{margin-top:22px;border-top:1px solid #2b4f76;padding-top:10px;text-align:center;font-size:11px}
.footer-bar nav{display:flex;justify-content:center;gap:18px;margin-bottom:6px}
</style>
</head>
<body>
<header class="site-header">
  <nav class="main-nav">
    <a class="is-active" href="#">home</a><a href="#">who we are</a><a href="#">what we do</a><a href="#">meet the team</a><a href="#">work with us</a><a href="#">contact us</a>
  </nav>
  <div class="brand"><span class="brand-dot"></span>quorvan</div>
  <div class="brand-sub">healthcare education</div>
  <h1 class="tagline">make the decision that we can do<br>what you are looking for</h1>
</header>

<section class="services">
  <p class="services-lead">At Quorvan we are healthcare communication specialists; this means we're scientists, journalists and marketers rolled into one.</p>
  <p class="services-intro">As you can see we provide all the things you'd expect from a top-class healthcare communications agency, but we have the depth of technical understanding and creative flair to produce sophisticated and memorable materials and programs, including:</p>
  <div class="service-grid">
    <div class="service"><div class="service-art" role="img" aria-label="Illustration of a stethoscope and clipboard"></div><p>Strategic tools for brand promotion (such as detail aids, product monographs, slide kits and patient materials)</p></div>
    <div class="service"><div class="service-art" role="img" aria-label="Illustration of a microscope and test tubes"></div><p>Non-promotional materials for market education (e.g. clinical papers and scientific summaries)</p></div>
    <div class="service"><div class="service-art" role="img" aria-label="Illustration of medicine bottles and tablets"></div><p>Complete programs such as clinical audits and product familiarisation programs</p></div>
    <div class="service"><div class="service-art" role="img" aria-label="Illustration of surgical instruments"></div><p>Medical meetings and symposia</p></div>
  </div>
</section>

<section class="prelaunch">
  <h2>Looking for something different pre-launch?</h2>
  <p>Quorvan has developed a unique tool for the earliest management of drug delivery, ideal for implementation in early access and special access programs. Each of these tools is designed around accredited education for practising healthcare professionals, and we work closely with our professional partners to deliver programs that meet every standard.</p>
</section>

<section class="team">
  <h2>meet the quorvan team</h2>
  <div class="team-list">
    <div class="member"><div class="member-photo" role="img" aria-label="Team member portrait"></div><div class="member-name">Doug Harrow</div><div class="member-role">Managing Director</div></div>
    <div class="member"><div class="member-photo" role="img" aria-label="Team member portrait"></div><div class="member-name">Doug Harrow</div><div class="member-role">Managing Director</div></div>
    <div class="member"><div class="member-photo" role="img" aria-label="Team member portrait"></div><div class="member-name">Doug Harrow</div><div class="member-role">Managing Director</div></div>
    <div class="member"><div class="member-photo" role="img" aria-label="Team member portrait"></div><div class="member-name">Doug Harrow</div><div class="member-role">Managing Director</div></div>
    <div class="member"><div class="member-photo" role="img" aria-label="Team member portrait"></div><div class="member-name">Doug Harrow</div><div class="member-role">Managing Director</div></div>
  </div>
</section>

<section class="location" role="img" aria-label="Street map showing the office location">
  <div class="address-card">Quorvan Healthcare Education<br>Level 3, 18 Calder Street<br>Northvale NSW 2099<br>Australia</div>
</section>

<footer class="site-footer">
  <div class="footer-cols">
    <div class="footer-col"><h3>Promotion</h3><ul><li>detail aids</li><li>mailers</li><li>newsletters</li><li>slide kits</li><li>posters</li><li>product monographs</li><li>communication campaigns</li></ul></div>
    <div class="footer-col"><h3>Education</h3><ul><li>clinical papers</li><li>evidence summaries</li><li>scientific newsletters</li><li>patient booklets</li><li>accredited educational activities</li></ul></div>
    <div class="footer-col"><h3>Programs</h3><ul><li>clinical audits</li><li>drug delivery programs</li><li>product familiarisation programs</li><li>patient support activities</li></ul></div>
    <div class="footer-col"><h3>Meetings</h3><ul><li>symposia and conference design</li><li>management and execution</li><li>advisory boards</li><li>KOL briefing groups</li></ul></div>
    <div class="footer-col social"><h3>Get in touch with us</h3><ul><li><span></span>Newsfeed</li><li><span></span>Updates</li><li><span></span>Community</li><li><span></span>Network</li></ul></div>
  </div>
  <div class="footer-bar">
    <nav><span>home</span><span>who we are</span><span>what we do</span><span>meet the team</span><span>work with us</span><span>contact us</span></nav>
    <div>© 2013 quorvan.net.au · hello@quorvan.net.au · Company number +61 2 5550 0142</div>
  </div>
</footer>
</body>
</html>
```